Business cards to launch an education platform

Hi,
I am looking at having new business cards designed.
I am a startup, developing a web platform for schools and university, the education world. It's an online assessment system.
I would like a card that looks classy, and that is using the colors and the font of my logo.

I have attached:
1) my logo
2) A business card that I have designed quickly so you can have all the information required in the card, but I really don't like it.
3) The font that I am using (Lato Regular) to design my web platform
4) Some screenshots of my web platform so you can have a look at the style that I have.

Target Market(s)

Major market: Education system: Schools and university
Minor markets: Business in general

Industry/Entity Type

Business

Contact Information for Business Card

Lydia Marsh
Director

M: 0437 681 902
E: lydia.marsh@copperLeafSystems.com.au

Requirements
Must have
• The colors of my logo

```html
<!DOCTYPE html>
<html lang="en">
<head>
<meta charset="utf-8">
<title>Copper Leaf Systems – Business Cards</title>
<link rel="stylesheet" href="https://fonts.googleapis.com/css2?family=Lato:wght@400;700&display=swap">
<style>
  :root {
    --navy: #0d4a80;
    --navy-deep: #0a3c6a;
    --sky: #2bb7e6;
    --white: #ffffff;
    --backdrop: #e9ebee;
    --ink-muted: #cfe3f3;
  }
  * { box-sizing: border-box; margin: 0; padding: 0; }
  html, body {
    width: 1200px; height: 950px; overflow: hidden;
    background: var(--backdrop);
    font-family: "Lato", sans-serif;
  }
  .canvas {
    position: relative; width: 1200px; height: 950px;
  }
  .card {
    position: absolute; left: 270px; width: 660px; height: 400px;
    border-radius: 4px; overflow: hidden;
    box-shadow: 0 10px 30px rgba(0,0,0,.18);
  }
  /* Back of card */
  .card-back {
    top: 50px;
    background: linear-gradient(135deg, #115593 0%, var(--navy) 50%, var(--navy-deep) 100%);
    display: flex; flex-direction: column; align-items: center; justify-content: center;
    color: var(--white);
  }
  .brand {
    display: flex; align-items: center; gap: 18px;
  }
  .brand-mark {
    width: 54px; height: 54px; background: var(--white);
  }
  .brand-name {
    font-weight: 400; font-size: 34px; letter-spacing: 3px; color: var(--white);
  }
  .card-back .website {
    margin-top: 70px; font-size: 17px; letter-spacing: 2px; color: var(--white);
  }
  /* Front of card */
  .card-front {
    top: 500px; background: var(--white);
  }
  .band-sky {
    position: absolute; left: 0; top: 170px; width: 100%; height: 125px;
    background: var(--sky);
  }
  .band-navy {
    position: absolute; left: 0; top: 295px; width: 100%; height: 105px;
    background: var(--navy);
  }
  .card-front .brand {
    position: absolute; left: 70px; top: 62px;
  }
  .card-front .brand-mark { width: 72px; height: 72px; background: var(--sky); }
  .card-front .brand-name { color: var(--navy); font-size: 40px; }
  .person {
    position: absolute; left: 0; top: 188px; width: 100%; text-align: center;
  }
  .person-name {
    font-weight: 700; font-size: 24px; letter-spacing: 1px; color: var(--navy);
    text-transform: uppercase;
  }
  .person-role {
    font-size: 15px; letter-spacing: 1px; color: var(--navy); margin-top: 4px;
    text-transform: uppercase;
  }
  .contact {
    position: absolute; left: 0; width: 100%;
    display: flex; align-items: center; justify-content: center; gap: 12px;
    color: var(--white); font-size: 19px;
  }
  .contact-phone { top: 255px; }
  .contact-email { top: 335px; }
  .contact svg { flex: none; }
</style>
</head>
<body>
<main class="canvas">
  <section class="card card-back" aria-label="Card back">
    <div class="brand">
      <span class="brand-mark"></span>
      <span class="brand-name">Copper Leaf Systems</span>
    </div>
    <p class="website">www.copperLeafSystems.com.au</p>
  </section>

  <section class="card card-front" aria-label="Card front">
    <div class="band-sky"></div>
    <div class="band-navy"></div>
    <div class="brand">
      <span class="brand-mark"></span>
      <span class="brand-name">Copper Leaf Systems</span>
    </div>
    <div class="person">
      <p class="person-name">Lydia Marsh</p>
      <p class="person-role">Director</p>
    </div>
    <p class="contact contact-phone">
      <svg width="14" height="22" viewBox="0 0 14 22" aria-hidden="true">
        <rect x="1" y="1" width="12" height="20" rx="2" fill="none" stroke="#fff" stroke-width="2"/>
        <circle cx="7" cy="17" r="1.4" fill="#fff"/>
      </svg>
      <span>0437 681 902</span>
    </p>
    <p class="contact contact-email">
      <svg width="22" height="16" viewBox="0 0 22 16" aria-hidden="true">
        <rect x="0" y="0" width="22" height="16" rx="1" fill="#fff"/>
        <path d="M1 1 L11 9 L21 1" fill="none" stroke="#0d4a80" stroke-width="1.6"/>
      </svg>
      <span>lydia.marsh@copperLeafSystems.com.au</span>
    </p>
  </section>
</main>
</body>
</html>
```